'Ormel Property Development' Business Card

Business Card Features:

High Quality (potentially textured) thick card - preference is white textured card

Logo (supplied)

We plan to use the vertical logo as the main logo. But i am happy for people to use either if they find it works better for the design of the card.

The building icon and also the insert to the 'E' is in a metallic finish, i think this should be finished in a metallic embossed or raised style.
Updates

Please note i have attached both a horizontal and Vertical Logo for your reference. We plan to use the vertical logo as the main logo. But i am happy for people to use either if they find it works better for the design of the card.

Please note i am considering having the cards made on stainless steel. This introduces the option of having cut outs in the card and etching or printing for the design. If you have a good concept for this please submit.

http://www.tinquarry.example/black-metal-cards# this is a site that makes the metal cards to offer some direction . . . . Please note i am basic the selection o the best design, if that means normal print cards on paper then this is what i will choose. But there are some great options with the metal. Thanks.

Industry/Entity Type

Building

Requirements
Must have
• Helvetica font to details side of card - logo as supplied to opposite side.

Card Details:

Darrow Pketts
Managing Director

+61 487 263 518
+61 3 6172 4809

PO Box 73
Kelmarsh, VIC 3187

darrow@ormel.example

www.ormel.example

```html
<!DOCTYPE html>
<html lang="en">
<head>
<meta charset="utf-8">
<title>Ormel Property Development – Business Card</title>
<link rel="stylesheet" href="https://fonts.googleapis.com/css2?family=Arimo:wght@400;700&display=swap">
<style>
  :root {
    --backdrop: #e4c89e;
    --card-black: #08090a;
    --card-sheen: #1b1c1e;
    --accent-gold: #e4c89e;
    --tagline-grey: #a7a7a7;
    --name-grey: #a3a3a3;
    --detail-grey: #b3b3b3;
    --icon-grey: #a6a6a6;
  }
  html, body {
    margin: 0;
    padding: 0;
    width: 1200px;
    height: 859px;
    overflow: hidden;
    background: var(--backdrop);
    font-family: "Arimo", "Helvetica Neue", Helvetica, Arial, sans-serif;
  }
  .card {
    position: absolute;
    left: 56px;
    top: 102px;
    width: 1088px;
    height: 620px;
    border-radius: 72px;
    background:
      radial-gradient(ellipse 520px 300px at 62% 48%, var(--card-sheen), transparent 75%),
      var(--card-black);
    overflow: hidden;
  }
  .brand {
    position: absolute;
    left: 64px;
    top: 0;
    width: 360px;
    height: 100%;
  }
  .brand-mark {
    position: absolute;
    left: 105px;
    top: 112px;
    width: 150px;
    height: 150px;
    background: var(--accent-gold);
  }
  .brand-name {
    position: absolute;
    left: 0;
    top: 306px;
    width: 100%;
    text-align: center;
    color: var(--accent-gold);
    font-size: 116px;
    font-weight: 700;
    line-height: 1;
    letter-spacing: 1px;
  }
  .brand-tagline {
    position: absolute;
    left: 0;
    top: 432px;
    width: 100%;
    text-align: center;
    color: var(--tagline-grey);
    font-size: 25px;
    font-weight: 700;
    font-variant: small-caps;
    letter-spacing: 0.5px;
    line-height: 1;
  }
  .divider {
    position: absolute;
    left: 494px;
    top: 84px;
    width: 5px;
    height: 455px;
    background: var(--accent-gold);
  }
  .person {
    position: absolute;
    left: 561px;
    top: 160px;
  }
  .person-name {
    margin: 0;
    font-size: 48px;
    font-weight: 400;
    color: var(--name-grey);
    letter-spacing: -0.5px;
    line-height: 1;
  }
  .person-title {
    margin: 14px 0 0;
    font-size: 23px;
    color: var(--name-grey);
    letter-spacing: 1.2px;
  }
  .contact-list {
    position: absolute;
    left: 562px;
    top: 352px;
    margin: 0;
    padding: 0;
    list-style: none;
  }
  .contact-item {
    display: flex;
    align-items: center;
    height: 48px;
    font-size: 24px;
    color: var(--detail-grey);
    white-space: nowrap;
  }
  .contact-icon {
    width: 26px;
    height: 26px;
    margin-right: 16px;
    flex: none;
  }
</style>
</head>
<body>
  <div class="card">
    <div class="brand">
      <div class="brand-mark"></div>
      <div class="brand-name">Ormel</div>
      <div class="brand-tagline">Property Development</div>
    </div>

    <div class="divider"></div>

    <div class="person">
      <h1 class="person-name">Darrow Pketts</h1>
      <p class="person-title">Managing Director</p>
    </div>

    <ul class="contact-list">
      <li class="contact-item">
        <svg class="contact-icon" viewBox="0 0 26 26" aria-hidden="true">
          <rect width="26" height="26" rx="4" fill="var(--icon-grey)"/>
          <path d="M8 5.5c1 0 2.2 2.8 2.2 3.6 0 .9-1.4 1.3-1.4 2.2 0 1.3 3.6 5 4.9 5 .9 0 1.3-1.4 2.2-1.4.8 0 3.6 1.2 3.6 2.2 0 1.6-2 3.3-3.6 3.3C11.3 20.4 5.6 14.7 5.6 9.1 5.6 7.5 6.4 5.5 8 5.5z" fill="var(--card-black)"/>
        </svg>
        +61 487 263 518, +61 3 6172 4809
      </li>
      <li class="contact-item">
        <svg class="contact-icon" viewBox="0 0 26 26" aria-hidden="true">
          <rect width="26" height="26" rx="4" fill="var(--icon-grey)"/>
          <path d="M13 4.5a6 6 0 0 1 6 6c0 4.3-6 11-6 11s-6-6.7-6-11a6 6 0 0 1 6-6z" fill="var(--card-black)"/>
          <circle cx="13" cy="10.5" r="2.3" fill="var(--icon-grey)"/>
        </svg>
        PO Box 73, Kelmarsh, VIC 3187
      </li>
      <li class="contact-item">
        <svg class="contact-icon" viewBox="0 0 26 26" aria-hidden="true">
          <rect width="26" height="26" rx="4" fill="var(--icon-grey)"/>
          <rect x="5" y="8" width="16" height="11" rx="1" fill="none" stroke="var(--card-black)" stroke-width="1.6"/>
          <path d="M5.5 8.5 13 14.5l7.5-6" fill="none" stroke="var(--card-black)" stroke-width="1.6"/>
        </svg>
        darrow@ormel.example
      </li>
      <li class="contact-item">
        <svg class="contact-icon" viewBox="0 0 26 26" aria-hidden="true">
          <g fill="none" stroke="var(--icon-grey)" stroke-width="1.6">
            <circle cx="13" cy="13" r="11"/>
            <ellipse cx="13" cy="13" rx="5" ry="11"/>
            <path d="M2 13h22M4 7.5h18M4 18.5h18M13 2v22"/>
          </g>
        </svg>
        www.ormel.example
      </li>
    </ul>
  </div>
</body>
</html>
```